Dynamic banner stand for Canadian music education charity

Harmonia Studios Canada offers music exams and other programs to instrumental and vocal students across Canada. We are looking to offer flexible, progressive, and more modern programs than our more traditional competitors. We need a new banner stand for our office that concisely demonstrated and illustrates our current identity materials while messaging what we do, directing interested people to our website. We have a previous banner stand that was designed for a separate purpose that is uploaded for reference, as well as our logo. We are hoping to match the look and feel of the previous banner stand as closely as possible, with the same or similar fonts, some similar layout, with similar shapes, graphics and colours. The new banner stand does not copy information from the old banner (uploaded for reference) but instead includes the following detail: Logo (uploaded), the following descriptor: "Progressive and innovative music education, assessment and performance training for students across Canada". This should be in a font that is modern, engaging, similar to the old banner stand (uploaded), yet conveys some element of tradition and authority. The banner also includes "Discover more at www.harmoniastudioscanada.ca" The banner should also include the same red/white/grey colour scheme as the old one, with similar background graphics that evoke fun and creativity in a modern way. Again, this design has new content as described here, and does not copy the content from the uploaded banner - it is only included for reference as to look and feel. The new banner should copy the original schemes to provide us with continuity in our marketing materials.

Target Market(s)

General public that is passing by our office

Font styles to use
Other font styles liked:
• See uploaded banner for reference

Colors
f04a50

Requirements
Must have
• Similar look and feel to previous banner (uploaded)
Nice to have
• Please see project description for more detail
Should not have
• Radical departure from current look and feel.

```html
<!DOCTYPE html>
<html lang="en">
<head>
<meta charset="utf-8">
<title>Harmonia Studios Canada – Banner Stand</title>
<link rel="stylesheet" href="https://fonts.googleapis.com/css2?family=Outfit:wght@300;400;600;700&display=swap">
<style>
  :root {
    --backdrop: #3d3d3d;
    --paper: #ffffff;
    --ink: #0a0a0a;
    --brand-red: #ee0000;
    --deep-red: #9e0000;
    --grey: #a9a9a9;
  }
  * { margin: 0; padding: 0; box-sizing: border-box; }
  html, body { width: 1200px; height: 1200px; overflow: hidden; background: var(--backdrop); }
  body { position: relative; font-family: "Outfit", sans-serif; }

  .banner {
    position: absolute;
    left: 352px; top: 3px;
    width: 495px; height: 1197px;
    background: var(--paper);
    overflow: hidden;
  }

  .brand {
    position: absolute;
    left: 76px; top: 45px;
    display: flex; align-items: center; gap: 16px;
  }
  .brand-square {
    width: 90px; height: 90px;
    background: var(--brand-red);
    border-radius: 10px;
    flex: none;
  }
  .brand-name {
    color: var(--brand-red);
    font-weight: 400;
    font-size: 30px;
    line-height: 1.1;
    width: 230px;
  }

  .descriptor {
    position: absolute;
    left: 45px; top: 319px;
    width: 440px;
    font-size: 40px;
    line-height: 46px;
    font-weight: 300;
    color: var(--ink);
    white-space: nowrap;
  }
  .descriptor .line { display: block; }
  .descriptor .line-lead { line-height: 62px; }
  .descriptor .lead {
    font-weight: 700;
    font-size: 54px;
    letter-spacing: 0.3px;
  }
  .descriptor .focus { color: var(--brand-red); font-weight: 400; }

  .footer-band {
    position: absolute;
    left: 0; top: 903px;
    width: 495px; height: 297px;
    background: var(--brand-red);
  }
  .footer-art {
    position: absolute;
    left: 0; top: 0;
    width: 255px; height: 297px;
    background: linear-gradient(135deg, var(--deep-red) 0%, var(--grey) 55%, var(--paper) 100%);
  }

  .cta {
    position: absolute;
    left: 250px; top: 112px;
    width: 240px;
    text-align: center;
    color: var(--paper);
    font-size: 14.5px;
    font-weight: 300;
    line-height: 19px;
    letter-spacing: 0.3px;
  }
</style>
</head>
<body>
  <main class="banner">
    <header class="brand">
      <span class="brand-square"></span>
      <span class="brand-name">Harmonia Studios Canada</span>
    </header>

    <h1 class="descriptor">
      <span class="line line-lead"><span class="lead">Progressive and</span></span>
      <span class="line line-lead"><span class="lead">innovative</span> <span class="focus">music</span></span>
      <span class="line focus">education, assessment</span>
      <span class="line focus">and performance</span>
      <span class="line">training for students</span>
      <span class="line">across Canada</span>
    </h1>

    <section class="footer-band">
      <div class="footer-art" role="img" aria-label="Decorative graphic of layered red, grey and white geometric squares"></div>
      <p class="cta">Discover more at<br>www.harmoniastudioscanada.ca</p>
    </section>
  </main>
</body>
</html>
```